Brio Patch Design

We need packaging design for the front and back of a 4.5 x 3.5 inch blister card. It needs a hole to hang from. The product is a pad of 30 peel and stick inspirational notes each with a different message.

Attached are an example of the card layout and pictures of examples of product use. Examples of these or other product use should be incorporated in the packaging design.

"Made in USA" should appear on the front and back.

Be creative, have fun with it.

Contact us with any questions.

To all interested parties:

Please see update to must-have section for this project.
Thank you.

People that are inclined to give out inspirational messages.

Product

• Made in USA. Examples, pictures, of products in use.

We would like to have a few pictures (see original attachments) or drawings on the front of the card to show examples of how the notes are used; in a coffee cup, on the mirror, on the computer screen, etc.

This is a pivotal part of the marketing for the product in that it should provide a quick visual understanding to the customer of how the notes are intended to be used.

Also, can you please replace the following words with the proper symbols; Vornaleaf, Quellix, Recycling, and add Daskovine.

```html
<!DOCTYPE html>
<html lang="en">
<head>
<meta charset="utf-8">
<title>Brio Patch – Blister Card Back</title>
<link rel="stylesheet" href="https://fonts.googleapis.com/css2?family=Arimo:wght@400&display=swap">
<style>
  :root {
    --sky-top: #05adf4;
    --sky-mid: #3ba3d9;
    --sky-bottom: #3c7dc6;
    --orange: #f7ad45;
    --lime: #b8cc18;
    --magenta: #d81f7e;
    --paper: #ffffff;
    --ink: #111111;
    --recycle-green: #5cc23a;
    --shadow: rgba(0, 0, 0, 0.35);
  }
  * { margin: 0; padding: 0; box-sizing: border-box; }
  html, body { width: 1200px; height: 1000px; overflow: hidden; }
  body { font-family: "Arimo", Arial, sans-serif; color: var(--ink); }

  .card-back {
    position: relative;
    width: 1200px;
    height: 1000px;
    overflow: hidden;
    background: linear-gradient(180deg, var(--sky-top) 0%, var(--sky-mid) 40%, var(--sky-mid) 60%, var(--sky-bottom) 100%);
  }

  .hang-hole { position: absolute; left: 530px; top: 40px; }

  .panel { position: absolute; box-shadow: 3px 4px 5px var(--shadow); }

  .panel--lime {
    left: 230px; top: 348px; width: 970px; height: 264px;
    background: var(--lime);
    padding: 26px 0 0 237px;
    font-size: 27px; line-height: 31px; letter-spacing: -0.3px;
  }
  .product-line__title { margin-bottom: 31px; }

  .panel--orange {
    left: 0; top: 108px; width: 408px; height: 368px;
    background: var(--orange);
    padding: 24px 0 0 10px;
    font-size: 27px; line-height: 31.3px; letter-spacing: -0.2px;
  }

  .panel--warning {
    left: 0; top: 636px; width: 870px; height: 84px;
    background: var(--paper);
    padding: 18px 0 0 13px;
    font-size: 27px; line-height: 31px; letter-spacing: -0.2px;
  }

  .panel--contact {
    left: 870px; top: 583px; width: 330px; height: 417px;
    background: var(--magenta);
    padding: 40px 0 0 36px;
    font-size: 27px; line-height: 31px; letter-spacing: -0.3px;
    box-shadow: -3px 3px 5px var(--shadow);
  }
  .contact-address { font-style: normal; }

  .social-list {
    position: absolute; left: 36px; bottom: 38px;
    list-style: none;
    display: flex; gap: 18px;
  }
  .social-list li {
    display: flex; align-items: center; gap: 8px;
    font-size: 27px; line-height: 40px; color: var(--paper);
  }
  .social-list .mark {
    width: 26px; height: 26px; background: var(--paper); border-radius: 4px;
  }

  .origin-badge {
    position: absolute; left: 72px; top: 888px;
    display: flex; align-items: center; gap: 10px;
  }
  .origin-badge__text {
    font-size: 29px; line-height: 29px; text-align: center; letter-spacing: 0;
  }
  .origin-badge__recycle {
    width: 78px; height: 78px; border-radius: 50%;
    background: var(--recycle-green);
    margin-top: 6px;
  }
</style>
</head>
<body>
  <main class="card-back">
    <svg class="hang-hole" width="175" height="66" viewBox="0 0 175 66" aria-hidden="true">
      <defs>
        <linearGradient id="holeShade" x1="0" y1="0" x2="0" y2="1">
          <stop offset="0" stop-color="#bdbdbd"/>
          <stop offset="0.5" stop-color="#f4f4f4"/>
          <stop offset="1" stop-color="#d0d0d0"/>
        </linearGradient>
      </defs>
      <path d="M22 28 H72 C76 10 98 4 104 4 C112 4 118 12 120 26 H150 C166 26 170 40 170 44 C170 56 162 62 150 62 H22 C8 62 4 54 4 45 C4 34 10 28 22 28 Z"
            fill="url(#holeShade)" stroke="#9a9a9a" stroke-width="1"/>
    </svg>

    <section class="panel panel--lime product-line">
      <p class="product-line__title">Brio Patch product line:</p>
      <p>Romantic for Her/Him •<br>
      Sexy for Her/Him • Parents for Kids • Motivational for<br>
      Teachers, Bosses, Coaches, etc. • Inspirational/Spiritual •<br>
      Coupons for Her, Him, Lovers, Kids • Treasure Hunt</p>
    </section>

    <section class="panel panel--orange intro">
      <p>Everyone likes to be reminded<br>
      of how valuable they are.<br>
      Leaving someone a little note<br>
      tucked in a drawer, on the<br>
      bathroom mirror, on a computer,<br>
      or even in a coffee cup is a great<br>
      way to show your appreciation<br>
      and add some joy to their lives<br>
      and yours. Be creative, use them<br>
      to stimulate your relationships.</p>
    </section>

    <section class="panel panel--warning warning">
      <p>Warning: Test on all surfaces. Colors could bleed when wet, glue could<br>leave a mark.</p>
    </section>

    <section class="panel panel--contact contact">
      <address class="contact-address">
        Brio Patch<br>
        PO Box 4410<br>
        Fernridge, OR 97999<br>
        503 555 0142<br>
        WWW.BrioPatch.com
      </address>
      <ul class="social-list">
        <li><span class="mark"></span>Vornaleaf</li>
        <li><span class="mark"></span>Quellix</li>
      </ul>
    </section>

    <div class="origin-badge">
      <p class="origin-badge__text">MADE<br>IN<br>USA</p>
      <div class="origin-badge__recycle" role="img" aria-label="Recycling symbol"></div>
    </div>
  </main>
</body>
</html>
```